Redesign of outdated "Automotive Automation Company"

We are looking to finally update our outdated website with some cutting edge graphics. We want our customers to know we value technology and are cutting edge as far as design. We provide automation solutions for the automotive industry which essentially means we program robots, and sell automation related products.

Current URL

http://lnk.vemrota.com/Qx7pwe
Updates

Project Deadline Extended
Reason: The client portal wasn't working, it's just finally been fixed by Pixel Harbor. I will go through and start reviewing designs.

We are trying to go with the same look and feel on our business cards, line cards, apparel, etc. so we are forming a brand. I have included the current draft of the line card. Please utilize our newest Logo TLV Standardized Logo.jpg http://img.solvarenpics.com/pz3Tm8d.jpg?1 Also we are trying hard to sell the following software / hardware companies so we can put some emphasis on their product. Meridel Controls https://www.meridelcontrols.com/ We make money on selling the software and then on the integration. I think you should tie in this animation. ยท From Shop Chaos to Smooth Output https://media.vorplexclips.com/deliveries/938127a4b51dfe03c7724bde1209f74a615b830c.jpg?image_play_button=true&image_play_button_color=7b796ae0&image_crop_resized=275x155 In this 2-minute video, discover how Quellwave can help run your plant floor. We are Authorized Integrators / Resellers for Tamberly Mechatronics Varnoth Sensorik http://varnoth.com/en/usa/ Meridel Controls https://www.meridelcontrols.com/ Corvane Process Works www.cpwkx.com Halberd Transfer Corp www.halberdtransfer.com Pennwick Machining http://www.pennwickmachining.com/strategic_partners.aspx

Target Market(s)

Large automotive companies looking for automation or robotic programming. So Professional is key.

Industry/Entity Type

Automotive

Font styles to use
Other font styles liked:
• Possible Open Sans or Lato

Colors
0591cc
ceeaf6
fbd4d5
fbf289
fece3e

Requirements
Must have
• Professional Modern Design.

I want a homepage design, and a rough Sales Page... Where numerous products can be listed.
Nice to have
• Maybe an updated logo if possible.

```html
<!DOCTYPE html>
<html lang="en">
<head>
<meta charset="utf-8">
<title>TLV Engineering Solutions</title>
<link href="https://fonts.googleapis.com/css2?family=Open+Sans:wght@400;600;700&display=swap" rel="stylesheet">
<style>
:root{
  --blue:#0591cc;
  --blue-dark:#0a6c9c;
  --blue-pale:#ceeaf6;
  --green:#6cb33f;
  --green-dark:#4f9427;
  --orange:#f2a12a;
  --text:#4a4a4a;
  --muted:#8a8a8a;
  --line:#dfe6ea;
  --page:#f4f7f9;
  --white:#ffffff;
}
*{margin:0;padding:0;box-sizing:border-box}
html,body{width:691px;height:1200px;overflow:hidden}
body{font-family:"Open Sans",Arial,sans-serif;color:var(--text);background:var(--page);font-size:6px;line-height:1.5;position:relative}
.page{position:absolute;left:0;top:0;width:691px;height:1200px}
.wrap{position:absolute;left:60px;width:571px}

/* header */
.brand{position:absolute;left:60px;top:10px;display:flex;align-items:center;gap:6px}
.brand-mark{width:24px;height:24px;border-radius:50%;background:var(--blue)}
.brand-name{font-size:19px;font-weight:700;color:var(--blue);letter-spacing:1px}
.brand-tag{position:absolute;left:60px;top:40px;font-size:5.5px;color:var(--text);letter-spacing:.5px}
.contact-top{position:absolute;right:60px;top:12px;text-align:right}
.contact-top .phone{font-size:11px;font-weight:700;color:var(--blue);line-height:1.3}
.contact-top .mail{font-size:6px;color:var(--muted)}
.social{position:absolute;right:60px;top:44px;display:flex;gap:3px}
.social span{width:13px;height:13px;border-radius:2px;background:var(--blue)}
.social span:nth-child(2){background:#46b3e6}
.social span:nth-child(3){background:#c8412f}

/* content panel */
.panel{position:absolute;left:52px;top:64px;width:587px;height:380px;background:var(--white);box-shadow:0 1px 6px rgba(0,0,0,.08)}
.nav{top:68px;height:17px;background:var(--white);border-bottom:1px solid var(--line);display:flex}
.nav a{font-size:5.5px;font-weight:700;color:var(--text);text-decoration:none;padding:0 11px;line-height:17px}
.nav a.active{background:var(--blue);color:var(--white)}
.hero{top:86px;height:258px;overflow:hidden;
  background:
    radial-gradient(ellipse 180px 140px at 62% 38%,rgba(250,250,248,.95),rgba(250,250,248,0) 70%),
    radial-gradient(ellipse 140px 120px at 30% 45%,rgba(122,128,132,.55),rgba(122,128,132,0) 70%),
    radial-gradient(ellipse 160px 70px at 75% 95%,rgba(96,150,150,.55),rgba(96,150,150,0) 70%),
    linear-gradient(180deg,#e9ecee 0%,#c7ccd0 40%,#9ea6ab 75%,#7d8a8c 100%);}
.hero:after{content:"";position:absolute;left:0;right:0;bottom:0;height:70px;background:linear-gradient(180deg,rgba(255,255,255,0),rgba(255,255,255,.25))}
.hero-box{position:absolute;left:0;top:172px;width:250px;height:62px;background:rgba(255,255,255,.9);border-left:4px solid var(--blue);padding:7px 10px;z-index:1}
.hero-box h2{font-size:12px;font-weight:700;color:var(--blue);line-height:1.2}
.hero-box h3{font-size:10px;font-weight:600;color:var(--blue-dark);line-height:1.3}
.hero-box p{font-size:4.5px;color:var(--muted);margin-top:2px}
.btn-contact{position:absolute;left:385px;top:190px;width:120px;height:28px;background:linear-gradient(var(--green),var(--green-dark));color:var(--white);font-size:10px;font-weight:700;text-align:center;line-height:28px;border-radius:3px;z-index:1;box-shadow:0 1px 3px rgba(0,0,0,.25)}

/* welcome */
.welcome{top:354px}
.welcome h1{font-size:13px;font-weight:400;color:var(--text);line-height:1.3}
.welcome h1 b{color:var(--blue);font-weight:700}
.welcome .sub{font-size:6.5px;color:var(--muted);margin-bottom:7px}
.welcome .lead{font-size:6px;font-weight:600;margin-bottom:2px}
.welcome p{font-size:5.5px;color:var(--muted)}

/* services */
.services-band{position:absolute;left:0;top:452px;width:691px;height:180px}
.services{top:486px;text-align:center}
.section-title{font-size:13px;color:var(--text);font-weight:400}
.section-title b{color:var(--blue);font-weight:700}
.service-grid{display:flex;gap:16px;margin-top:18px;text-align:left}
.service{flex:1}
.service h4{font-size:7px;font-weight:700;color:var(--text);margin-bottom:3px}
.service p{font-size:5px;color:var(--muted)}
.more{display:inline-block;margin-top:5px;font-size:4.5px;padding:1px 6px;border:1px solid #b7c3ca;border-radius:2px;color:var(--muted);background:var(--white)}

/* values */
.values{position:absolute;left:150px;top:612px;width:391px;height:245px}
.values-photo{position:absolute;left:0;top:0;width:391px;height:205px;
  background:
    radial-gradient(ellipse 70px 80px at 22% 55%,rgba(190,168,150,.55),rgba(190,168,150,0) 70%),
    radial-gradient(ellipse 70px 80px at 50% 45%,rgba(168,172,178,.6),rgba(168,172,178,0) 70%),
    radial-gradient(ellipse 70px 80px at 78% 55%,rgba(186,170,158,.55),rgba(186,170,158,0) 70%),
    linear-gradient(180deg,#f4f7f9 0%,#e7eaec 30%,#d6dadd 100%);
  -webkit-mask-image:linear-gradient(180deg,transparent 0%,#000 25%);mask-image:linear-gradient(180deg,transparent 0%,#000 25%)}
.value{position:absolute;border-radius:50%;color:var(--white);font-weight:700;text-align:center;display:flex;align-items:center;justify-content:center;border:3px solid var(--white);box-shadow:0 2px 5px rgba(0,0,0,.25);line-height:1.35}
.v1{left:45px;top:160px;width:70px;height:70px;background:radial-gradient(circle at 40% 35%,#2aa9de,var(--blue));font-size:7px}
.v2{left:155px;top:152px;width:82px;height:82px;background:radial-gradient(circle at 40% 35%,#f8bb4d,var(--orange));font-size:7.5px}
.v3{left:276px;top:160px;width:70px;height:70px;background:radial-gradient(circle at 40% 35%,#86c85a,var(--green));font-size:7px}

/* testimonials + blog */
.say{position:absolute;left:60px;top:893px;width:260px}
.blog{position:absolute;left:360px;top:893px;width:271px}
.col-title{font-size:12px;text-align:center;position:relative;font-weight:400}
.col-title b{color:var(--blue);font-weight:700}
.col-title:before,.col-title:after{content:"";position:absolute;top:9px;width:80px;border-top:1px solid var(--line)}
.col-title:before{left:0}.col-title:after{right:0}
.quote{margin-top:20px;display:flex;gap:8px}
.quote-mark{font-size:22px;color:#c9d3d9;line-height:1}
.quote p{font-size:5.5px;color:var(--muted)}
.author{margin-top:10px;margin-left:64px;display:flex;align-items:center;gap:6px;font-size:5.5px}
.avatar{width:22px;height:22px;border-radius:50%;background:linear-gradient(#c8cdd1,#9aa2a8)}
.post{display:flex;gap:8px;margin-top:10px}
.post:first-of-type{margin-top:16px}
.thumb{width:30px;height:26px;background:linear-gradient(135deg,#9fb0bb,#dfe5e9)}
.post .date{font-size:5px;font-weight:700}
.post p{font-size:5px;color:var(--muted)}

/* footer */
.footer{position:absolute;left:0;top:1096px;width:691px;height:72px;background:var(--blue-pale)}
.foot-cols{position:absolute;left:60px;top:14px;width:571px;display:flex;justify-content:space-between}
.foot-item{display:flex;gap:6px}
.foot-icon{width:16px;height:16px;border-radius:50%;background:var(--blue);display:flex;align-items:center;justify-content:center}
.foot-item h5{font-size:6px;font-weight:700}
.foot-item p{font-size:5px;color:var(--muted)}
.foot-item .ph{font-size:7px;font-weight:700;color:var(--blue)}
.foot-social{display:flex;gap:3px;margin-top:3px}
.foot-social span{width:11px;height:11px;border-radius:2px;background:var(--blue)}
.bottom{position:absolute;left:60px;top:1176px;width:571px;display:flex;justify-content:space-between;align-items:center;font-size:5px;color:var(--muted)}
.cards{display:flex;gap:3px}
.cards span{width:16px;height:10px;border-radius:1px;background:#c4ccd2}
.bottom-links a{color:var(--muted);text-decoration:none;margin-left:8px}
</style>
</head>
<body>
<div class="page">
  <div class="brand"><span class="brand-mark"></span><span class="brand-name">TLV</span></div>
  <div class="brand-tag">Automation · Robotic · Control</div>
  <div class="contact-top">
    <div class="phone">1-855-ROBO-TLV</div>
    <div class="mail">info@tlvengsolutions.com</div>
  </div>
  <div class="social"><span></span><span></span><span></span><span></span></div>

  <div class="panel"></div>
  <nav class="wrap nav">
    <a class="active">HOME</a><a>ABOUT US</a><a>SERVICES</a><a>CONTACT US</a>
  </nav>
  <div class="wrap hero" role="img" aria-label="Industrial robot arm on a factory floor">
    <div class="hero-box">
      <h2>PROVIDING SOLUTIONS</h2>
      <h3>for Automation, Robotics and Controls</h3>
      <p>We deliver smart integration for plants that need reliable output. Our team works with leading vendors to improve your lines.</p>
    </div>
    <div class="btn-contact">CONTACT US</div>
  </div>

  <section class="wrap welcome">
    <h1>Welcome to <b>TLV Engineering Solutions inc</b></h1>
    <div class="sub">Your Premier Automation Consulting &amp; Systems Integration Partner</div>
    <div class="lead">Helping your business optimize its automation</div>
    <p>Our engineers help manufacturers stay ahead with proven controls, robotic programming and system integration. We study your process, design the right solution and support it long after start-up, so your lines run faster, safer and with fewer stops. From a single cell to a full plant, we bring the same care to every project and every customer we serve.</p>
  </section>

  <svg class="services-band" viewBox="0 0 691 180" preserveAspectRatio="none" aria-hidden="true">
    <defs><linearGradient id="band" x1="0" y1="0" x2="0" y2="1"><stop offset="0" stop-color="#ceeaf6"/><stop offset="1" stop-color="#f4f7f9"/></linearGradient></defs>
    <path d="M0 20 Q345 -8 691 20 L691 180 L0 180 Z" fill="url(#band)"/>
    <path d="M0 24 Q345 -4 691 24" fill="none" stroke="#ffffff" stroke-width="2"/>
  </svg>

  <section class="wrap services">
    <h2 class="section-title">Our <b>Services</b></h2>
    <div class="service-grid">
      <div class="service"><h4>Controls Engineering</h4><p>Design of PLC, HMI and safety systems built for uptime and clear diagnostics on every line.</p><span class="more">read more</span></div>
      <div class="service"><h4>Design Engineering</h4><p>Mechanical and electrical layouts that fit your plant, your budget and your schedule.</p><span class="more">read more</span></div>
      <div class="service"><h4>Design Specification</h4><p>Clear specs for equipment, robots and software so every vendor builds the same plan.</p><span class="more">read more</span></div>
      <div class="service"><h4>Field Installation</h4><p>On site install, start-up and robot programming with training for your own crews.</p><span class="more">read more</span></div>
    </div>
  </section>

  <div class="values">
    <div class="values-photo" role="img" aria-label="Group of engineers in hard hats behind the value circles"></div>
    <div class="value v1">Our<br>Philosophy</div>
    <div class="value v2">Our<br>Commitment<br>to Results</div>
    <div class="value v3">Our<br>Experience</div>
  </div>

  <section class="say">
    <h2 class="col-title">What <b>Say</b></h2>
    <div class="quote"><span class="quote-mark">“</span><p>The team delivered our new robot cell ahead of plan and trained our staff well. Downtime dropped in the first month and the support has been quick every time we called.</p></div>
    <div class="author"><span class="avatar" role="img" aria-label="Client portrait"></span><span>Lorem Client</span></div>
  </section>

  <section class="blog">
    <h2 class="col-title">Latest <b>Blog</b></h2>
    <div class="post"><span class="thumb" role="img" aria-label="Blog photo"></span><div><div class="date">3 Nov 2014</div><p>New tools for faster robot programming on busy assembly lines.</p></div></div>
    <div class="post"><span class="thumb" role="img" aria-label="Blog photo"></span><div><div class="date">2 Nov 2014</div><p>How modern controls cut scrap and keep your plant running.</p></div></div>
    <div class="post"><span class="thumb" role="img" aria-label="Blog photo"></span><div><div class="date">1 Nov 2014</div><p>Five steps to plan a smooth start-up for your next cell.</p></div></div>
  </section>

  <footer class="footer">
    <div class="foot-cols">
      <div class="foot-item">
        <span class="foot-icon"><svg width="8" height="8" viewBox="0 0 10 10"><path d="M5 0a3.5 3.5 0 0 0-3.5 3.5C1.5 6 5 10 5 10s3.5-4 3.5-6.5A3.5 3.5 0 0 0 5 0z" fill="#fff"/><circle cx="5" cy="3.5" r="1.3" fill="#0591cc"/></svg></span>
        <div><h5>Location</h5><p>48 Kestrel Row,<br>Lorwick, MI 49011</p></div>
      </div>
      <div class="foot-item">
        <span class="foot-icon"><svg width="8" height="8" viewBox="0 0 10 10"><rect x="0.5" y="2" width="9" height="6" fill="none" stroke="#fff"/><path d="M0.5 2L5 5.5 9.5 2" fill="none" stroke="#fff"/></svg></span>
        <div><h5>Email</h5><p>info@tlvengsolutions.com</p></div>
      </div>
      <div class="foot-item">
        <span class="foot-icon"><svg width="8" height="8" viewBox="0 0 10 10"><path d="M2 1l2 2-1 1.5c.6 1.2 1.3 1.9 2.5 2.5L7 6l2 2-1.2 1.5C4.5 9 1 5.5.5 2.2z" fill="#fff"/></svg></span>
        <div><h5>Phone</h5><p class="ph">1-855-ROBO-TLV</p></div>
      </div>
      <div class="foot-item">
        <div><h5>Connect with us</h5><div class="foot-social"><span></span><span></span><span></span><span></span></div></div>
      </div>
    </div>
  </footer>
  <div class="bottom">
    <span>© 2014 TLV Engineering Solutions Inc.</span>
    <span class="cards"><span></span><span></span><span></span></span>
    <span class="bottom-links"><a>Privacy</a><a>Terms &amp; Conditions</a><a>Contact Us</a></span>
  </div>
</div>
</body>
</html>
```